Business card design

I need my logo on this card, things I need the card to have on it
licensed and insured.
owner operators Derek & Milton Halvorsen
my phone number 5418237906
Disaster Recovery, Storm Damage Restoration, Proactive Disaster Plan Management, Roof Repair/Restoration Structural Repair and Reconstruction, Emergency Boarding and Tarping Service, Perimeter Fencing, Emergency Tree Removal,

```html
<!DOCTYPE html>
<html lang="en">
<head>
<meta charset="utf-8">
<title>Halvorsen's Construction L.L.C – Business Card</title>
<link rel="stylesheet" href="https://fonts.googleapis.com/css2?family=Montserrat:wght@400;500;600&display=swap">
<style>
  :root {
    --backdrop: #969696;
    --card: #ffffff;
    --brand-blue: #1b98e8;
    --slate: #6f7276;
    --rule: #8a8a8a;
    --pale-blue: #d8ebf9;
    --pale-grey: #e6e6e6;
  }
  * { box-sizing: border-box; margin: 0; padding: 0; }
  html, body { width: 1200px; height: 1200px; overflow: hidden; }
  body {
    background: var(--backdrop);
    font-family: "Montserrat", sans-serif;
    position: relative;
  }
  .card {
    position: absolute;
    left: 226px;
    width: 746px;
    height: 436px;
    background: var(--card);
    border-radius: 26px;
    overflow: hidden;
  }
  .card--front { top: 95px; }
  .card--back { top: 614px; }

  /* Front */
  .front-name {
    position: absolute;
    left: 0; right: 0;
    top: 210px;
    text-align: center;
    color: var(--brand-blue);
    font-weight: 400;
    line-height: 1;
  }
  .front-name .name-main { display: block; font-size: 60px; letter-spacing: 1px; }
  .front-name .name-sub { display: block; font-size: 19px; letter-spacing: 8px; margin-top: 12px; }
  .license-badge {
    position: absolute;
    left: 580px; top: 56px;
    width: 120px; height: 120px;
  }
  .license-badge text {
    font-family: "Montserrat", sans-serif;
    font-size: 9.5px;
    font-weight: 500;
    fill: var(--slate);
  }
  .divider {
    position: absolute;
    left: 33px; right: 33px;
    top: 336px;
    border-top: 1px solid var(--rule);
  }
  .services {
    position: absolute;
    left: 0; right: 0;
    top: 349px;
    text-align: center;
    color: var(--slate);
    font-size: 12.4px;
    font-weight: 500;
    line-height: 19.5px;
    text-transform: uppercase;
  }
  .services .dot { color: var(--brand-blue); margin: 0 2px; }

  /* Back */
  .back-decoration {
    position: absolute;
    left: 0; top: 0;
    width: 746px; height: 436px;
  }
  .back-name {
    position: absolute;
    left: 52px; top: 130px;
    color: var(--brand-blue);
    font-weight: 400;
    line-height: 1;
  }
  .back-name .name-main { display: block; font-size: 32px; letter-spacing: 0.5px; }
  .back-name .name-sub { display: block; font-size: 11px; letter-spacing: 4.4px; margin-top: 6px; }
  .owners {
    position: absolute;
    left: 48px; top: 232px;
    width: 346px;
    text-align: center;
  }
  .owners .owner-names {
    color: var(--brand-blue);
    font-size: 26px;
    font-weight: 600;
  }
  .owners .owner-role {
    margin-top: 8px;
    color: var(--slate);
    font-size: 14px;
    font-weight: 500;
    letter-spacing: 3px;
  }
  .phone-pill {
    position: absolute;
    left: 98px; top: 345px;
    width: 243px; height: 40px;
    border: 2px solid var(--brand-blue);
    border-radius: 20px;
    display: flex;
    align-items: center;
    padding-left: 3px;
    gap: 6px;
    color: var(--brand-blue);
    font-size: 22px;
    font-weight: 600;
  }
  .phone-pill svg { width: 30px; height: 30px; flex: none; }
</style>
</head>
<body>

<section class="card card--front">
  <div class="front-name">
    <span class="name-main">HALVORSEN'S</span>
    <span class="name-sub">CONSTRUCTION L.L.C</span>
  </div>

  <svg class="license-badge" viewBox="0 0 120 120" role="img" aria-label="Licensed and insured seal">
    <defs>
      <path id="seal-ring" d="M60 60 m-49 0 a49 49 0 1 1 98 0 a49 49 0 1 1 -98 0"/>
    </defs>
    <text><textPath href="#seal-ring" textLength="300" lengthAdjust="spacing">LICENSED &amp; INSURED • LICENSED &amp; INSURED •</textPath></text>
    <path d="M40 60 L54 74 L82 42" fill="none" stroke="var(--brand-blue)" stroke-width="9" stroke-linejoin="round"/>
  </svg>

  <div class="divider"></div>

  <p class="services">
    Disaster Recovery <span class="dot">•</span> Storm Damage Restoration <span class="dot">•</span> Proactive Disaster Plan<br>
    Management <span class="dot">•</span> Roof Repair/Restoration Structural Repair and Reconstruction<br>
    Emergency Boarding and Tarping Service <span class="dot">•</span> Perimeter Fencing <span class="dot">•</span> Emergency Tree Removal
  </p>
</section>

<section class="card card--back">
  <svg class="back-decoration" viewBox="0 0 746 436" aria-hidden="true">
    <rect x="300" y="-40" width="560" height="560" fill="var(--pale-blue)" opacity="0.55"/>
    <rect x="560" y="0" width="200" height="436" fill="var(--pale-grey)" opacity="0.7"/>
  </svg>

  <div class="back-name">
    <span class="name-main">HALVORSEN'S</span>
    <span class="name-sub">CONSTRUCTION L.L.C</span>
  </div>

  <div class="owners">
    <p class="owner-names">Derek &amp; Milton Halvorsen</p>
    <p class="owner-role">OWNER OPERATORS</p>
  </div>

  <div class="phone-pill">
    <svg viewBox="0 0 30 30" aria-hidden="true">
      <circle cx="15" cy="15" r="15" fill="var(--brand-blue)"/>
      <path d="M10.5 7.5c.6-.4 1.4-.3 1.8.3l1.6 2.4c.4.6.3 1.3-.2 1.7l-1.1.9c.8 1.8 2.2 3.2 3.9 4l.9-1.1c.4-.5 1.2-.6 1.7-.2l2.4 1.6c.6.4.7 1.2.3 1.8l-.9 1.3c-.6.8-1.6 1.2-2.6.9-4.4-1.3-7.9-4.8-9.2-9.2-.3-1 .1-2 .9-2.6z" fill="#fff"/>
    </svg>
    <span class="phone-number">(541) 823 - 7906</span>
  </div>
</section>

</body>
</html>
```